Business Card Design Project

Want a modern business card.
Concern is that our email address is long and thus poses a design challenge.
Items like the company name can be omitted from text as it will be available via the logo.

Example:
Gerald Tunstall
President / CEO
Cell 555.304.1182
Office 555.617.2093
geraldt@korvantsolutionsgroup.example
www.korvantsolutionsgroup.example

Target Market(s)

Technical and executive level members of Information Technology companies in the Healthcare industry.

Industry/Entity Type

Business

Colors

Designer to choose colors to be used in the design.

Requirements
Nice to have
• Raised logo, but I am open.

```html
<!DOCTYPE html>
<html lang="en">
<head>
<meta charset="utf-8">
<title>Korvant Solutions Group – Business Card</title>
<link rel="stylesheet" href="https://fonts.googleapis.com/css2?family=Open+Sans:wght@400;600;700&display=swap">
<style>
  :root {
    --navy: #1b3f8a;
    --navy-deep: #0f2a66;
    --navy-light: #3566b0;
    --red: #d42a2a;
    --paper: #ffffff;
    --ink: #222222;
    --backdrop: #e9e9ec;
  }
  * { margin: 0; padding: 0; box-sizing: border-box; }
  html, body {
    width: 1200px; height: 913px; overflow: hidden;
    background: var(--backdrop);
    font-family: "Open Sans", Arial, sans-serif;
  }
  .sheet {
    position: relative; width: 1200px; height: 913px;
    display: flex; flex-direction: column; align-items: center; justify-content: center; gap: 60px;
  }
  .card {
    position: relative; width: 600px; height: 343px; overflow: hidden;
    box-shadow: 0 6px 18px rgba(0,0,0,.18);
  }
  .card-front {
    background: linear-gradient(160deg, var(--navy-light) 0%, var(--navy) 45%, var(--navy-deep) 100%);
    display: flex; align-items: center; justify-content: center;
  }
  .wordmark {
    font-weight: 700; letter-spacing: 2px; text-transform: uppercase;
    line-height: 1.05; text-align: right;
  }
  .wordmark .line-main { display: block; font-size: 36px; }
  .wordmark .line-sub { display: block; font-size: 20px; letter-spacing: 4px; }
  .card-front .wordmark { color: var(--paper); }

  .card-back { background: var(--paper); }
  .card-back .waves { position: absolute; inset: 0; }
  .card-back .wordmark {
    position: absolute; left: 40px; top: 46px; color: var(--navy);
  }
  .card-back .wordmark .line-main { font-size: 26px; letter-spacing: 1.5px; }
  .card-back .wordmark .line-sub { font-size: 14px; letter-spacing: 3px; }

  .holder {
    position: absolute; right: 18px; top: 188px; text-align: right; color: var(--paper);
  }
  .holder-name { font-size: 14px; font-weight: 700; }
  .holder-title { font-size: 10px; font-weight: 400; margin-top: 1px; }

  .contact {
    position: absolute; left: 40px; top: 186px; list-style: none;
    color: var(--ink); font-size: 13px; line-height: 21px;
  }
  .contact li { display: flex; align-items: center; gap: 6px; }
  .contact svg { width: 12px; height: 12px; fill: var(--navy); flex: none; }
</style>
</head>
<body>
<main class="sheet">

  <section class="card card-front" aria-label="Card front">
    <div class="wordmark">
      <span class="line-main">Korvant Solutions</span>
      <span class="line-sub">Group</span>
    </div>
  </section>

  <section class="card card-back" aria-label="Card back">
    <svg class="waves" viewBox="0 0 600 343" preserveAspectRatio="none" aria-hidden="true">
      <path d="M560 0 C530 180 430 300 0 322 L0 343 L600 343 L600 0 Z" fill="var(--navy)"/>
      <path d="M546 0 C516 180 416 298 0 312" fill="none" stroke="var(--red)" stroke-width="7"/>
      <path d="M532 0 C502 178 402 294 0 301" fill="none" stroke="var(--red)" stroke-width="2.5"/>
    </svg>

    <div class="wordmark">
      <span class="line-main">Korvant Solutions</span>
      <span class="line-sub">Group</span>
    </div>

    <div class="holder">
      <p class="holder-name">Gerald Tunstall</p>
      <p class="holder-title">President / CEO</p>
    </div>

    <ul class="contact">
      <li>
        <svg viewBox="0 0 16 16"><rect x="4" y="1" width="8" height="14" rx="1.5"/><rect x="5.5" y="3" width="5" height="8" fill="#fff"/></svg>
        555.304.1182
        <svg viewBox="0 0 16 16"><path d="M2 6c0-2 2-3 6-3s6 1 6 3v1h-3V5.5H5V7H2z"/><path d="M4 8h8l2 6H2z"/></svg>
        555.617.2093
      </li>
      <li>
        <svg viewBox="0 0 16 16"><path d="M1 3h14v10H1z"/><path d="M1 3l7 6 7-6" fill="none" stroke="#fff" stroke-width="1.3"/></svg>
        geraldt@korvantsolutionsgroup.example
      </li>
      <li>
        <svg viewBox="0 0 16 16"><circle cx="8" cy="8" r="7"/><path d="M1 8h14M8 1c-3 3-3 11 0 14M8 1c3 3 3 11 0 14" fill="none" stroke="#fff" stroke-width="1"/></svg>
        www.korvantsolutionsgroup.example
      </li>
    </ul>
  </section>

</main>
</body>
</html>
```